Roll Up Design Velumo

We are a beauty company and we need stunning design for our general roll-up banner that we gonna place just next to the main gate of mall that we are located in. The most important for us is the quality, accuracy and the unity of poster. It has to be super elegant, engaging and beautiful. Has to match our service standards (high). Colors do not matter as long as the overall look is exciting.
Examples and our logo are attached
Updates
Reason: We need more designs (more creativity, more quality, colurs and proportions).
Target Market(s)
Middle class ladies, students, business women
Industry/Entity Type
It Company
Colors
Designer to choose colors to be used in the design.
Look and feel
Each slider illustrates characteristics of the customer's brand and the style your logo design should communicate.

```html
<!DOCTYPE html>
<html lang="az">
<head>
<meta charset="utf-8">
<title>Velumo Gözəllik – Roll-up</title>
<link rel="stylesheet" href="https://fonts.googleapis.com/css2?family=Open+Sans:wdth,wght@75..100,400&family=Roboto+Condensed:wght@400;700&display=swap">
<style>
:root{
  --night:#151515;
  --night-soft:#3a3a3a;
  --satin-light:#f4e8e2;
  --satin-mid:#e6d3ca;
  --satin-deep:#cdb2a5;
  --gold-light:#f2d58a;
  --gold-deep:#a8802f;
  --bronze:#8c6a4c;
  --bronze-dark:#6a4a31;
  --cocoa:#6b4429;
  --white:#ffffff;
}
*{margin:0;padding:0;box-sizing:border-box}
html,body{width:1200px;height:2857px;overflow:hidden;background:var(--white)}
.banner{position:relative;width:1200px;height:2857px;overflow:hidden;
  background:linear-gradient(170deg,var(--satin-light) 0%,var(--satin-mid) 55%,var(--satin-deep) 100%)}
.banner-art{position:absolute;inset:0;width:1200px;height:2857px}
.brand{position:absolute;top:58px;left:0;width:1200px;text-align:center;color:var(--white);
  font-family:"Roboto Condensed",sans-serif}
.brand-name{font-weight:700;font-size:170px;line-height:170px;letter-spacing:14px;text-transform:uppercase}
.brand-rule{width:600px;height:3px;background:var(--white);margin:30px auto 26px;opacity:.9}
.brand-sub{font-weight:400;font-size:66px;line-height:70px;letter-spacing:4px}
.tagline{position:absolute;left:660px;top:548px;color:var(--white);
  font-family:"Roboto Condensed",sans-serif;font-weight:700;font-size:96px;line-height:100px}
.phones{position:absolute;left:760px;top:1030px;width:380px;color:var(--white);
  font-family:"Roboto Condensed",sans-serif;font-weight:400;font-size:58px;line-height:67px}
.service-cloud text{font-family:"Open Sans",sans-serif;fill:var(--cocoa)}
.service-cloud .narrow{font-stretch:75%}
.email{position:absolute;left:0;width:1200px;top:2545px;text-align:center;color:var(--bronze-dark);
  font-family:"Roboto Condensed",sans-serif;font-weight:700;font-size:102px;line-height:110px}
.web-band{position:absolute;left:0;top:2664px;width:1200px;height:193px;
  background:linear-gradient(180deg,#b58f62 0%,var(--bronze) 45%,#5e4230 100%);
  display:flex;align-items:center;justify-content:center}
.web-address{color:var(--white);font-family:"Roboto Condensed",sans-serif;font-weight:700;font-size:104px;line-height:110px}
</style>
</head>
<body>
<main class="banner">
  <svg class="banner-art" viewBox="0 0 1200 2857" xmlns="http://www.w3.org/2000/svg">
    <defs>
      <radialGradient id="studioGlow" cx="0.55" cy="0.35" r="0.8">
        <stop offset="0" stop-color="var(--night-soft)"/>
        <stop offset="1" stop-color="var(--night)"/>
      </radialGradient>
      <linearGradient id="portraitTone" x1="0" y1="0" x2="1" y2="1">
        <stop offset="0" stop-color="#1e1a19"/>
        <stop offset="0.5" stop-color="#5a413a"/>
        <stop offset="1" stop-color="#2a2222"/>
      </linearGradient>
      <linearGradient id="goldSweep" x1="0" y1="1" x2="1" y2="0">
        <stop offset="0" stop-color="var(--gold-deep)"/>
        <stop offset="0.5" stop-color="var(--gold-light)"/>
        <stop offset="1" stop-color="var(--gold-deep)"/>
      </linearGradient>
      <linearGradient id="drapeTone" x1="0" y1="0" x2="1" y2="0">
        <stop offset="0" stop-color="#f7eee9"/>
        <stop offset="0.5" stop-color="#d9c1b5"/>
        <stop offset="1" stop-color="#e9d9d1" stop-opacity="0"/>
      </linearGradient>
      <clipPath id="darkArea">
        <path d="M0 0 H1200 V745 C900 900 520 1070 0 1092 Z"/>
      </clipPath>
    </defs>

    <rect x="0" y="1090" width="230" height="1460" fill="url(#drapeTone)" role="img" aria-label="Folded satin drape along the left edge"/>

    <path class="header-dark" d="M0 0 H1200 V745 C900 900 520 1070 0 1092 Z" fill="url(#studioGlow)"/>
    <rect x="70" y="300" width="740" height="800" clip-path="url(#darkArea)" fill="url(#portraitTone)" role="img" aria-label="Portrait of a woman with long dark curly hair and red lips"/>
    <path class="gold-swoosh" d="M0 1092 C520 1070 900 900 1200 745 V785 C900 930 520 1085 0 1104 Z" fill="url(#goldSweep)"/>

    <g class="phone-badge" fill="var(--bronze)" transform="translate(950 1168)">
      <rect x="-180" y="-180" width="360" height="360"/>
      <rect x="-180" y="-180" width="360" height="360" transform="rotate(15)"/>
      <rect x="-180" y="-180" width="360" height="360" transform="rotate(30)"/>
      <rect x="-180" y="-180" width="360" height="360" transform="rotate(45)"/>
      <rect x="-180" y="-180" width="360" height="360" transform="rotate(60)"/>
      <rect x="-180" y="-180" width="360" height="360" transform="rotate(75)"/>
      <circle r="220"/>
    </g>

    <g class="service-cloud">
      <text x="154" y="1427" font-size="57">Laser Hair Removal</text>
      <text class="narrow" x="211" y="1505" font-size="50">Laser Hair Removal</text>
      <text x="609" y="1509" font-size="40">Laser Hair Removal</text>
      <text x="264" y="1576" font-size="57">Laser Hair Removal</text>
      <text x="495" y="1647" font-size="57">Laser Hair Removal</text>
      <text x="182" y="1684" font-size="40">Laser Hair Removal</text>
      <text x="651" y="1702" font-size="40">Laser Hair Removal</text>
      <text x="264" y="1756" font-size="57">Laser Hair Removal</text>
      <text x="615" y="1814" font-size="44">Laser Hair Removal</text>
      <text x="165" y="1864" font-size="62">Laser Hair Removal</text>
      <text x="182" y="1929" font-size="35">Laser Hair Removal</text>
      <text x="550" y="1944" font-size="59">Laser Hair Removal</text>
      <text class="narrow" x="163" y="2002" font-size="55">Laser Hair Removal</text>
      <text x="560" y="2020" font-size="42">Laser Hair Removal</text>
      <text x="213" y="2085" font-size="55">Laser Hair Removal</text>
      <text x="444" y="2155" font-size="55">Laser Hair Removal</text>
      <text x="132" y="2197" font-size="40">Laser Hair Removal</text>
      <text x="598" y="2213" font-size="42">Laser Hair Removal</text>
      <text x="213" y="2265" font-size="55">Laser Hair Removal</text>
      <text x="567" y="2325" font-size="48">Laser Hair Removal</text>
      <text x="125" y="2382" font-size="59">Laser Hair Removal</text>
      <text x="631" y="2436" font-size="35">Laser Hair Removal</text>
    </g>
  </svg>

  <header class="brand">
    <div class="brand-name">Velumo</div>
    <div class="brand-rule"></div>
    <div class="brand-sub">GÖZƏLLİK</div>
  </header>

  <p class="tagline">Gözellik her<br>yandadir...</p>

  <ul class="phones" style="list-style:none">
    <li>(012) 555 0140</li>
    <li>(051) 555 0172</li>
    <li>(055) 555 0186</li>
    <li>(070) 555 0193</li>
  </ul>

  <p class="email">office@velumogozellik.com</p>

  <footer class="web-band">
    <p class="web-address">www.velumogozellik.com</p>
  </footer>
</main>
</body>
</html>
```